A tri fold flyer to be sent to parents advertising Learning Center, tutoring in math or language after school and on weekendsSince 1994 the Bright Path Learning Center has been helping the children on Oahu do better in school. Bright Path has developed a successful method of teaching math, reading and writing for students in grades K-12. Affordable and effective, it's unlike any other learning system.

Target Market(s)

Parents of school age kids

Industry/Entity Type

Education

Font styles to use
Sans Serif

Requirements
Must have
• same text as in previews
Nice to have
• 3 fold
Should not have
• mistakes

```html
<!DOCTYPE html>
<html lang="en">
<head>
<meta charset="utf-8">
<title>Bright Path Hawaii – Tri-fold Flyer</title>
<link href="https://fonts.googleapis.com/css2?family=Questrial&family=Montserrat:wght@600;700&display=swap" rel="stylesheet">
<style>
  :root {
    --stage: #2b2b2b;
    --gold: #f2b705;
    --gold-light: #fcd34d;
    --gold-deep: #d99a00;
    --ink: #111111;
    --paper: #ffffff;
    --paper-grey: #ececec;
    --text: #1c1c1c;
  }
  * { box-sizing: border-box; margin: 0; padding: 0; }
  html, body { width: 1200px; height: 900px; overflow: hidden; }
  body {
    background: var(--stage);
    font-family: "Questrial", "Century Gothic", sans-serif;
    color: var(--text);
  }
  .brochure {
    position: absolute; left: 60px; top: 60px;
    width: 1080px; height: 780px;
    display: flex;
    box-shadow: 0 10px 40px rgba(0,0,0,.5);
  }
  .panel { position: relative; width: 360px; height: 780px; overflow: hidden; }

  /* Left panel */
  .panel--testimonials { background: linear-gradient(180deg, var(--paper-grey), var(--paper) 40%, var(--paper-grey)); }
  .photo { position: absolute; }
  .photo--classroom { left: 0; top: 0; width: 360px; height: 250px; background: linear-gradient(135deg, #2f5a45, #6d8c78 55%, #e8e3dd); }
  .photo--study { left: 0; bottom: 0; width: 360px; height: 200px; background: linear-gradient(135deg, #d8d8d8, #8a8a8a 60%, #3c3c3c); }
  .testimonials { position: absolute; left: 26px; right: 20px; top: 262px; font-size: 12.4px; line-height: 1.32; }
  .testimonials__title { text-align: center; font-size: 14px; line-height: 1.3; margin-bottom: 12px; }
  .testimonials p { margin-bottom: 7px; }

  /* Middle panel */
  .panel--contact { background: linear-gradient(180deg, var(--gold-light), var(--gold) 60%, var(--gold-deep)); }
  .photo--tutor { left: 0; top: 0; width: 360px; height: 200px; background: linear-gradient(120deg, #f4f1ea, #c9d3dd 50%, #eef2f5); }
  .swoosh { position: absolute; left: 0; width: 360px; }
  .contact { position: absolute; left: 0; right: 0; top: 260px; text-align: center; }
  .brand-name { font-family: "Questrial", sans-serif; color: var(--ink); letter-spacing: 3px; line-height: 1.1; }
  .brand-name--small { font-size: 24px; display: flex; align-items: center; justify-content: center; gap: 10px; }
  .brand-mark { width: 14px; height: 14px; border-radius: 50%; background: var(--ink); }
  .offer { margin-top: 28px; font-size: 20px; line-height: 1.25; }
  .call { margin-top: 6px; font-size: 20px; display: flex; justify-content: center; align-items: center; gap: 6px; }
  .call strong { font-family: "Montserrat", sans-serif; font-weight: 700; }
  .alt-line { margin-top: 20px; font-size: 19px; line-height: 1.3; }
  .address { margin-top: 20px; font-size: 14px; line-height: 1.35; }
  .web-pill { display: inline-block; margin-top: 26px; background: var(--ink); color: var(--paper); font-size: 13px; padding: 6px 18px; border-radius: 14px; }

  /* Right panel */
  .panel--cover { background: var(--ink); }
  .cover-top { position: absolute; left: 0; top: 0; width: 360px; height: 200px; background: linear-gradient(180deg, var(--gold-light), var(--gold)); }
  .brand-name--large { position: absolute; top: 50px; left: 0; right: 0; text-align: center; font-size: 32px; }
  .photo--student { left: 0; top: 180px; width: 360px; height: 420px; background: linear-gradient(180deg, #f1f1f1, #cfcfcf 70%, #a7a7a7); }
  .cover-headline { position: absolute; left: 0; right: 0; top: 640px; text-align: center; }
  .cover-headline__tag { color: var(--gold); font-size: 31px; }
  .cover-headline__name { color: var(--paper); font-family: "Montserrat", sans-serif; font-weight: 700; font-size: 27px; margin-top: 2px; letter-spacing: .5px; }
  .phone-pill { display: inline-block; margin-top: 16px; background: var(--gold); color: var(--ink); font-size: 18px; padding: 3px 22px; border-radius: 14px; }
</style>
</head>
<body>
<main class="brochure">

  <section class="panel panel--testimonials">
    <div class="photo photo--classroom" role="img" aria-label="Photo of a cheering girl with two teachers in front of a chalkboard"></div>
    <div class="testimonials">
      <p class="testimonials__title">Bright Path Works:<br>These are comments from<br>Bright Path parents:</p>
      <p>"My son loves Bright Path classes; I noticed a big change in him toward his school work."</p>
      <p>" The 2/1 ratio and individualized support makes the program a success."</p>
      <p>"The staff at Bright Path is very helpful, friendly and just super!"</p>
      <p>"Bright Path really made my kids look forward to learning new things and to look forward to going to school."</p>
      <p>"My daughter has improved 90% with school."</p>
      <p>"all my children enjoyed their Bright Path classes. They all showed improvement in their grades"<br>"We are very pleased with the results." "Bright Path is the best investment I have made for my son!"</p>
    </div>
    <div class="photo photo--study" role="img" aria-label="Black and white photo of a teacher helping a young girl write"></div>
  </section>

  <section class="panel panel--contact">
    <div class="photo photo--tutor" role="img" aria-label="Photo of a tutor sitting with a thoughtful boy at a desk"></div>
    <svg class="swoosh" style="top:170px" width="360" height="80" viewBox="0 0 360 80" aria-hidden="true">
      <path d="M0 80 C120 20 240 10 360 30 L360 0 L0 0 Z" fill="#ffffff"/>
      <path d="M0 80 C120 20 240 10 360 30 L360 55 C240 40 120 60 0 95 Z" fill="#111111"/>
    </svg>
    <div class="contact">
      <div class="brand-name brand-name--small"><span class="brand-mark"></span>BRIGHT PATH<br>HAWAII</div>
      <p class="offer">For a FREE TEST and a<br>FREE TRIAL LESSON</p>
      <p class="call">Call
        <svg width="16" height="16" viewBox="0 0 24 24" aria-hidden="true"><path fill="#111" d="M6.6 10.8a15 15 0 0 0 6.6 6.6l2.2-2.2c.3-.3.7-.4 1-.2 1.1.4 2.3.6 3.6.6.6 0 1 .4 1 1V20c0 .6-.4 1-1 1A17 17 0 0 1 3 4c0-.6.4-1 1-1h3.5c.6 0 1 .4 1 1 0 1.3.2 2.5.6 3.6.1.3 0 .7-.2 1z"/></svg>
        <strong>555-0142</strong></p>
      <p class="alt-line">BRIGHT PATH HAWAII<br>555-PATH 555-0142</p>
      <p class="address">Harbor View Business Plaza<br>218 Lanakila Ave<br>Pearl City HI 96782</p>
      <span class="web-pill">www.brightpathhawaii.com</span>
    </div>
    <svg class="swoosh" style="bottom:0" width="360" height="130" viewBox="0 0 360 130" aria-hidden="true">
      <path d="M0 130 L0 60 C120 110 250 100 360 20 L360 130 Z" fill="#111111"/>
      <path d="M0 60 C120 110 250 100 360 20 L360 30 C250 110 120 120 0 72 Z" fill="#ffffff" opacity=".85"/>
    </svg>
  </section>

  <section class="panel panel--cover">
    <div class="cover-top">
      <div class="brand-name brand-name--large">BRIGHT PATH<br>HAWAII</div>
    </div>
    <div class="photo photo--student" role="img" aria-label="Photo of a smiling boy holding a small whiteboard"></div>
    <svg class="swoosh" style="top:150px" width="360" height="70" viewBox="0 0 360 70" aria-hidden="true">
      <path d="M0 30 C100 10 250 10 360 60 L360 0 L0 0 Z" fill="#f2b705"/>
      <path d="M0 30 C100 10 250 10 360 60 L360 68 C250 20 100 20 0 40 Z" fill="#111111"/>
    </svg>
    <svg class="swoosh" style="top:560px" width="360" height="80" viewBox="0 0 360 80" aria-hidden="true">
      <path d="M0 40 C120 10 250 10 360 0 L360 80 L0 80 Z" fill="#111111"/>
      <path d="M0 40 C120 10 250 10 360 0 L360 6 C250 18 120 20 0 48 Z" fill="#ffffff" opacity=".8"/>
    </svg>
    <div class="cover-headline">
      <p class="cover-headline__tag">I'm a Bright Path Kid!</p>
      <p class="cover-headline__name">BRIGHT PATH HAWAII</p>
      <span class="phone-pill">555-PATH 555-0142</span>
    </div>
  </section>

</main>
</body>
</html>
```